Brand new letterhead, business card, email signature etc.

We are a financial company in London, UK. Our website is www.quorvane.com. We're wanting a complete remodel of the company colours, letter head, business cards, email signatures, etc. Looking to keep the same font for the company name. I have upload a colour palette that we want to work with. We're looking for company letterhead for outgoing letters/ correspondence, letterhead for internal documentation, email signatures, e-letters. etc. Ultimately we will redesign the entire website also. It is important that our clients get a strong, secure, warm, trustworthy, solid feeling and first impression.
Updates

Designs look the same

Target Market(s)

Institutional investors, (ultra) high net worth individuals

Industry/Entity Type

Finance, Invesments banking.

Font styles to use
Other font styles liked:
• Current font is "Champagne & Limousines"

Requirements
Must have
• Must use the colours provided on the PDF uploaded to the portal. The purple = main colour. The red = accent colour.
Nice to have
• Nice to use same font as now for the company name "Marlowin". Font is "Champagne & Limousines". Nice to have some reference to the old logo flower, but only subtle.
Should not have
• Do not use the colour red from our website. Use the colours provided on the colour palette PDF that I uploaded in the portal.

```html
<!DOCTYPE html>
<html lang="en">
<head>
<meta charset="utf-8">
<title>Marlowin – Business Card</title>
<link href="https://fonts.googleapis.com/css2?family=Josefin+Sans:wght@300;400;600&display=swap" rel="stylesheet">
<style>
  :root {
    --page: #ffffff;
    --card: #fcfaf8;
    --card-edge: #8a8386;
    --plum: #4a2c36;
    --plum-soft: #7d636a;
    --accent-red: #d8262b;
    --salmon: #f0a186;
    --blush: #f6cfc2;
    --grey-band: #d4d0d1;
    --flower-grey: #e8e4e3;
    --flower-blush: #fbe3da;
  }
  * { box-sizing: border-box; margin: 0; padding: 0; }
  html, body { width: 1000px; height: 1200px; overflow: hidden; background: var(--page); }
  body { position: relative; font-family: "Josefin Sans", sans-serif; color: var(--plum); }

  .card {
    position: absolute; left: 312px; width: 378px; height: 245px;
    background: var(--card); border: 1px solid var(--card-edge); overflow: hidden;
  }
  .card--front { top: 320px; }
  .card--back { top: 636px; }

  .side-band { position: absolute; left: 0; top: 0; width: 8px; height: 138px; background: var(--grey-band); }
  .side-stripe { position: absolute; left: 8px; top: 0; width: 5px; height: 138px; background: var(--blush); }
  .rule-h { position: absolute; left: 0; top: 137px; width: 275px; height: 2px; background: var(--plum); }
  .rule-v { position: absolute; left: 273px; top: 137px; width: 2px; height: 108px; background: var(--plum); }

  .art { position: absolute; left: 275px; width: 103px; }
  .art--top { top: 0; height: 135px; background: linear-gradient(135deg, #f6f3f2, var(--flower-grey)); border-left: 1px solid var(--grey-band); }
  .art--mid { top: 138px; height: 58px; background: linear-gradient(135deg, var(--flower-blush), #fdf1ec); border-top: 3px solid var(--blush); }
  .art--low { top: 199px; height: 46px; background: linear-gradient(135deg, #f7f4f2, #ede9e7); border-top: 3px solid var(--blush); }

  .brand { position: absolute; left: 77px; top: 24px; display: flex; align-items: center; }
  .brand__mark { width: 42px; height: 42px; border: 1px solid var(--plum); flex: none; }
  .brand__name {
    margin-left: 10px; font-weight: 300; font-size: 18px; letter-spacing: 2px;
    color: var(--plum); line-height: 1; padding-top: 3px; white-space: nowrap;
  }

  .person { position: absolute; left: 78px; top: 89px; }
  .person__name { font-size: 16px; font-weight: 400; color: var(--plum-soft); letter-spacing: 0; white-space: nowrap; }
  .person__role { margin-top: 5px; font-size: 8.5px; color: var(--accent-red); white-space: nowrap; }

  .contacts { position: absolute; left: 54px; top: 156px; list-style: none; }
  .contacts li { display: flex; align-items: flex-start; font-size: 8.5px; line-height: 12.5px; margin-bottom: 6px; }
  .contacts svg { width: 16px; height: 16px; flex: none; margin-right: 8px; margin-top: -2px; }
  .contacts .text { width: 190px; color: var(--plum); }

  .tagline { position: absolute; left: 78px; top: 160px; font-size: 8.3px; line-height: 16.5px; color: var(--salmon); text-transform: uppercase; white-space: nowrap; }
  .web { position: absolute; left: 78px; top: 211px; font-size: 10.5px; color: var(--plum); }
</style>
</head>
<body>

<section class="card card--front" aria-label="Business card front">
  <div class="side-band"></div><div class="side-stripe"></div>
  <div class="brand"><div class="brand__mark"></div><span class="brand__name">MARLOWIN</span></div>
  <div class="person">
    <p class="person__name">EDRIC TOLVANE</p>
    <p class="person__role">Chair of the Governing Body</p>
  </div>
  <div class="rule-h"></div><div class="rule-v"></div>
  <ul class="contacts">
    <li>
      <svg viewBox="0 0 16 16" fill="none" stroke="#d8262b" stroke-width="1"><path d="M8 13.5s-4-4.2-4-7.2a4 4 0 0 1 8 0c0 3-4 7.2-4 7.2z"/><circle cx="8" cy="6.3" r="1.5"/><ellipse cx="8" cy="14" rx="4" ry="1.2"/></svg>
      <span class="text">Marlowin (IOM) Limited, Harrow Court, Ramsey, Isle of Man, IM98 4QT</span>
    </li>
    <li>
      <svg viewBox="0 0 16 16" fill="none" stroke="#d8262b" stroke-width="1"><rect x="4" y="1.5" width="8" height="13" rx="1"/><rect x="5.5" y="3.5" width="5" height="8"/><line x1="7" y1="13" x2="9" y2="13"/></svg>
      <span class="text">Marlowin Group Limited, 9th Floor, 14 Bellfield Row, London, EC3N 2LP</span>
    </li>
    <li>
      <svg viewBox="0 0 16 16" fill="none" stroke="#d8262b" stroke-width="1"><rect x="2" y="5" width="12" height="9"/><path d="M2 5l6 5 6-5"/><rect x="5" y="1.5" width="6" height="5"/></svg>
      <span class="text">info@marlowin.com</span>
    </li>
  </ul>
  <div class="art art--top" role="img" aria-label="Line drawing of a large flower in soft grey"></div>
  <div class="art art--mid" role="img" aria-label="Line drawing of petals in blush pink"></div>
  <div class="art art--low" role="img" aria-label="Faint line drawing of a flower in grey"></div>
</section>

<section class="card card--back" aria-label="Business card back">
  <div class="side-band"></div><div class="side-stripe"></div>
  <div class="brand" style="top:66px"><div class="brand__mark"></div><span class="brand__name">MARLOWIN</span></div>
  <div class="rule-h"></div><div class="rule-v"></div>
  <p class="tagline">Full-service brokerage dedicated<br>to the interests of experienced,<br>mid-market investors</p>
  <p class="web">www.quorvane.com</p>
  <div class="art art--top" role="img" aria-label="Line drawing of a large flower in soft grey"></div>
  <div class="art art--mid" role="img" aria-label="Line drawing of petals in blush pink"></div>
  <div class="art art--low" role="img" aria-label="Faint line drawing of a flower in grey"></div>
</section>

</body>
</html>
```